Excellent Rewards: Escort Services for Men needs Banner Ad Design

We need a banner ad design for a company based in Brazil called "Lunaré" (http://www.lunare-app.com.br), which offers escort services for men. Our main strength and focus is helping people easily search for escorts using mobile devices, by being an mobile optimized repository of escorts which are crawled from many non-mobile optimized sites.

Target Market(s)

Men at all ages (above 18) looking for escorts

Industry/Entity Type

Escort

Requirements
Must have
• Size must be 468x60
The logo must be on white background
Nice to have
• The banner could have an eye-catching animation

The banner could have a small and quick animation showing the usage of the mobile application (like navigating through the application).
Should not have
• If animated then the text should not be split between frames.

```html
<!DOCTYPE html>
<html lang="pt-BR">
<head>
<meta charset="utf-8">
<title>Lunaré – banner 468x60</title>
<link href="https://fonts.googleapis.com/css2?family=Ubuntu:wght@400;500;700&family=Open+Sans:wght@400;700&display=swap" rel="stylesheet">
<style>
  :root {
    --stage-bg: #2b2b2b;
    --stage-bg-dark: #222222;
    --caption: #e6e6e6;
    --banner-maroon: #7a1620;
    --banner-maroon-dark: #5a0f16;
    --brand-red: #a3182b;
    --logo-bg: #ffffff;
    --pitch-bg: #dfe4d3;
    --pitch-text: #2c2c2c;
    --screen-bg: #f4f4f4;
    --screen-text: #333333;
    --screen-muted: #8a8a8a;
    --arrow: #555555;
    --photo-tone-a: #e3c9a6;
    --photo-tone-b: #b88a5c;
    --hand-tone-a: #e8b79a;
    --hand-tone-b: #c98f72;
  }
  * { margin: 0; padding: 0; box-sizing: border-box; }
  html, body {
    width: 1200px; height: 507px; overflow: hidden;
    background: linear-gradient(135deg, var(--stage-bg), var(--stage-bg-dark));
  }
  .stage { position: relative; width: 1200px; height: 507px; }

  .banner {
    position: absolute; left: 43px; top: 0; width: 1114px; height: 148px;
    background: linear-gradient(180deg, var(--banner-maroon), var(--banner-maroon-dark));
    overflow: hidden;
  }
  .banner-logo {
    position: absolute; left: 0; top: 0; width: 267px; height: 148px;
    background: var(--logo-bg);
    display: flex; align-items: center; justify-content: center; gap: 14px;
  }
  .logo-dot { width: 34px; height: 34px; border-radius: 50%; background: var(--brand-red); }
  .logo-name {
    font-family: "Ubuntu", sans-serif; font-weight: 700; font-size: 52px;
    color: var(--brand-red); letter-spacing: -1px;
  }
  .banner-pitch {
    position: absolute; left: 279px; top: 10px; width: 436px; height: 128px;
    background: var(--pitch-bg); border-radius: 6px;
    display: flex; flex-direction: column; justify-content: center; align-items: center;
    font-family: "Open Sans", sans-serif; font-weight: 700; font-size: 27px;
    line-height: 1.28; color: var(--pitch-text); text-align: center;
  }
  .pitch-highlight { color: var(--brand-red); }

  .banner-app {
    position: absolute; left: 727px; top: 10px; width: 377px; height: 128px;
  }
  .app-screen {
    position: absolute; left: 0; top: 0; width: 340px; height: 128px;
    background: var(--screen-bg); border-radius: 6px; overflow: hidden;
  }
  .profile-photo {
    position: absolute; left: 10px; top: 10px; width: 108px; height: 108px;
    background: linear-gradient(160deg, var(--photo-tone-a), var(--photo-tone-b));
    border-radius: 4px;
  }
  .profile-name {
    position: absolute; left: 134px; top: 30px;
    font-family: "Open Sans", sans-serif; font-weight: 700; font-size: 30px; color: var(--screen-text);
  }
  .profile-fee {
    position: absolute; left: 134px; top: 74px;
    font-family: "Open Sans", sans-serif; font-size: 15px; color: var(--screen-muted);
  }
  .next-arrow { position: absolute; left: 312px; top: 51px; }
  .app-hand {
    position: absolute; left: 346px; top: 8px; width: 31px; height: 112px;
    background: linear-gradient(200deg, var(--hand-tone-a), var(--hand-tone-b));
    border-radius: 16px 6px 6px 16px;
  }

  .caption {
    position: absolute; left: 0; width: 1200px; text-align: center;
    font-family: "Ubuntu", sans-serif; font-weight: 700; color: var(--caption);
  }
  .caption-link { top: 208px; font-size: 48px; }
  .caption-ext { top: 322px; font-size: 52px; }
  .caption-size { top: 398px; font-size: 52px; }
</style>
</head>
<body>
<main class="stage">
  <section class="banner" aria-label="Banner Lunaré 468x60">
    <div class="banner-logo">
      <span class="logo-dot"></span>
      <span class="logo-name">Lunaré</span>
    </div>
    <div class="banner-pitch">
      <span>O maior catálogo de</span>
      <span class="pitch-highlight">acompanhantes</span>
      <span>na palma da sua mão.</span>
    </div>
    <div class="banner-app">
      <div class="app-screen">
        <div class="profile-photo" role="img" aria-label="Foto de perfil da acompanhante"></div>
        <span class="profile-name">Lívia</span>
        <span class="profile-fee">Cachê: R$ 200,00</span>
        <svg class="next-arrow" width="16" height="26" viewBox="0 0 16 26" aria-hidden="true">
          <polyline points="3,3 13,13 3,23" fill="none" stroke="var(--arrow)" stroke-width="4" stroke-linecap="round" stroke-linejoin="round"/>
        </svg>
      </div>
      <div class="app-hand" role="img" aria-label="Mão tocando a tela do celular"></div>
    </div>
  </section>

  <p class="caption caption-link">Link to animation in the description.</p>
  <p class="caption caption-ext">File extension: *.GIF</p>
  <p class="caption caption-size">File size: 267 KB</p>
</main>
</body>
</html>
```